Web site design for BrixaForm Software (www.brixaformsoftware.example)

Need the design as well as the html for the website. The brief is given in the attached file.
If possible, would like to use pencil sketches instead of images to give a unique look to the site.
Target Market(s)
small Software product companies
Industry/Entity Type
Software
Coding
Coded - Design and coding required
Number of Pages Required
5+ page

```html
<!DOCTYPE html>
<html lang="en">
<head>
<meta charset="utf-8">
<title>BrixaForm Software — Driven By Architecture</title>
<link href="https://fonts.googleapis.com/css2?family=Courier+Prime:ital,wght@0,400;0,700;1,400;1,700&family=Roboto+Condensed:wght@700&display=swap" rel="stylesheet">
<style>
  :root {
    --paper: #f1f1f0;
    --ink: #1a1a1a;
    --ink-soft: #3a3a3a;
    --bar: #1c1c1c;
    --bar-text: #ffffff;
    --sketch-light: #d9d9d6;
    --sketch-dark: #8a8a86;
  }
  * { box-sizing: border-box; margin: 0; padding: 0; }
  html, body { width: 1200px; height: 3789px; overflow: hidden; }
  body {
    position: relative;
    background: var(--paper);
    color: var(--ink);
    font-family: "Courier Prime", "Courier New", monospace;
  }
  .abs { position: absolute; }

  .top-nav {
    left: 0; top: 0; width: 1200px; height: 52px;
    background: var(--bar);
    display: flex; justify-content: center; align-items: center; gap: 30px;
    border-bottom: 4px solid #2e2e2e;
  }
  .top-nav a {
    font-family: "Roboto Condensed", Arial, sans-serif;
    font-weight: 700; font-size: 13px; letter-spacing: .5px;
    color: var(--bar-text); text-decoration: none; text-transform: uppercase;
  }

  .brand {
    left: 106px; top: 92px;
    font-size: 46px; font-weight: 700; letter-spacing: 9px; color: var(--ink);
    text-transform: uppercase;
  }
  .tagline { left: 860px; top: 106px; font-size: 18px; font-weight: 700; }

  .sketch {
    background: linear-gradient(160deg, var(--sketch-light), var(--sketch-dark));
    border-radius: 6px;
    opacity: .75;
  }

  .lead-quote {
    left: 645px; top: 258px; width: 475px;
    font-size: 26px; font-weight: 700; font-style: italic; line-height: 44px;
  }
  .lead-quote cite { display: block; margin-top: 14px; font-size: 18px; }

  .quote {
    font-size: 17px; font-style: italic; line-height: 26px; color: var(--ink-soft);
  }
  .quote cite { display: block; margin-top: 6px; font-size: 13px; font-weight: 700; line-height: 22px; }

  .copy {
    font-size: 18px; font-weight: 700; line-height: 35px;
  }
  .copy p + p { margin-top: 18px; }
  .copy.small { font-size: 14px; line-height: 22px; }
  .copy.small p + p { margin-top: 14px; }

  .dots { left: 0; top: 2185px; width: 1200px; height: 100px; }

  .section-title {
    left: 106px; top: 2366px;
    font-size: 26px; font-weight: 400; letter-spacing: 3px; text-transform: uppercase;
  }

  .footer {
    left: 0; top: 3733px; width: 1200px; height: 56px;
    background: var(--bar);
    display: flex; justify-content: flex-end; align-items: center; gap: 24px;
    padding-right: 126px;
  }
  .footer .social { width: 14px; height: 14px; border-radius: 50%; background: var(--bar-text); }
</style>
</head>
<body>

<nav class="abs top-nav">
  <a href="#">Home</a><a href="#">Services</a><a href="#">About Us</a><a href="#">Case Studies</a><a href="#">Accolades</a><a href="#">Giving Back</a><a href="#">Partners</a><a href="#">Blog</a><a href="#">Stories</a><a href="#">Contact Us</a>
</nav>

<div class="abs brand">BrixaForm</div>
<div class="abs tagline">Driven By Architecture</div>

<div class="abs sketch" style="left:126px;top:215px;width:304px;height:365px" role="img" aria-label="Pencil sketch of a craftsman at a workbench"></div>

<blockquote class="abs lead-quote">
  “Perfection is achieved not when there is nothing more to add, but when there is nothing left to take away.”
  <cite>-Aurel Vantremont</cite>
</blockquote>

<blockquote class="abs quote" style="left:106px;top:636px;width:470px">
  “We are what we repeatedly do. Excellence, then, is not an act, but a habit.”
  <cite>-Theron of Kallis</cite>
</blockquote>
<blockquote class="abs quote" style="left:621px;top:636px;width:480px">
  “Look deep into nature, and you will understand everything better”
  <cite>-Halvard Ostrem</cite>
</blockquote>
<blockquote class="abs quote" style="left:106px;top:766px;width:470px">
  “Though human ingenuity may make various inventions…it will never devise any inventions more beautiful, nor more simple, nor more to the purpose than Nature does; because in her inventions nothing is wanting, and nothing is superfluous.”
  <cite>— Corvino da Lenta, The Da Lenta Notebooks, Vol. II, XIV: Anatomy, Zoology and Physiology</cite>
</blockquote>

<div class="abs sketch" style="left:783px;top:758px;width:303px;height:278px" role="img" aria-label="Pencil sketch of a snail"></div>

<div class="abs copy" style="left:106px;top:1148px;width:480px">
  <p>Design pervades nature. Whether it is the unique symmetry of a snowflake, or the fibonnacci number of a sunflower or nautilus shell, or self replicating fractals, design is everywhere.</p>
</div>

<div class="abs sketch" style="left:620px;top:1150px;width:466px;height:290px" role="img" aria-label="Pencil sketch of a sunflower field"></div>
<div class="abs sketch" style="left:106px;top:1350px;width:324px;height:226px" role="img" aria-label="Pencil sketch of seashells"></div>

<div class="abs copy" style="left:620px;top:1452px;width:535px">
  <p>We love to explore new frontiers in technology - be it Predictive Analytics, Cognitive IOT or AI</p>
</div>

<div class="abs copy" style="left:106px;top:1626px;width:480px">
  <p>In todays world, Good Design is associated more with tangible products, and User interfaces. But good design has always been part of software engineering. Good design is what enables massive software edifices to remain stable. Good design is UI and UX of course, but it also the process of deciding "what" is required, "how" it is to be built, "who" will build it, and how will its goodness perpetuate itself.</p>
  <p>We are a small but eclectic group of seasoned programmers who infuse rigor and design into solid engineering in software.</p>
</div>

<div class="abs sketch" style="left:645px;top:1617px;width:340px;height:203px" role="img" aria-label="Pencil sketch of a cathedral"></div>

<div class="abs copy" style="left:620px;top:1866px;width:540px">
  <p>We infuse design into rigorous engineering - not only in software design and UI, but also by using design thinking for deciding what to build; using design for designing the organisational structure of hierarchies, collaborations and communities; for designing the most productive work spaces and processes; and also communities which perpetuate and replicate themselves.</p>
</div>

<svg class="abs dots" viewBox="0 0 1200 100" aria-hidden="true">
  <g fill="#111">
    <circle cx="215" cy="50" r="38"/><circle cx="404" cy="50" r="38"/><circle cx="594" cy="50" r="38"/><circle cx="783" cy="50" r="38"/><circle cx="973" cy="50" r="38"/>
  </g>
</svg>

<h2 class="abs section-title">Background and Expertise</h2>

<div class="abs copy small" style="left:106px;top:2436px;width:480px">
  <p>We are primarily server side programmers with expertise in large scale projects - be it Software development tools, Distributed software frameworks, Telecom and mediation software or Business intelligence.</p>
  <p>Over the years, we have been the trusted offshore product development partner for many startups and mid sized software product companies, and have built software products from scratch.</p>
  <p>We have built over 10 software products for startups all over the world. Best in class UI, and APIs have been designed and implemented by us. Often we take a core technology developed in a university, or an idea, and build a product around it.</p>
</div>

<div class="abs sketch" style="left:631px;top:2374px;width:455px;height:318px" role="img" aria-label="Pencil sketch of a temple tower"></div>

<div class="abs copy small" style="left:620px;top:2712px;width:480px">
  <p>We work in cloud, mobile apps, big data and analytics. We are now getting into predictive analytics, machine learning and AI.</p>
  <p>We conduct high end training in Scrum, clean code, and clean design inspired by Master Orrin. We conduct training in Jovel, and concurrency.</p>
</div>

<div class="abs sketch" style="left:106px;top:2778px;width:336px;height:280px" role="img" aria-label="Hand-drawn cloud with arrows diagram"></div>
<div class="abs sketch" style="left:620px;top:2895px;width:466px;height:270px" role="img" aria-label="Pencil sketch of a domed basilica"></div>

<div class="abs copy small" style="left:106px;top:3110px;width:480px">
  <p>We have been associated with the leaders of the Agile movement, and have expertise implementing agile practices in BrixaForm as well as other companies.</p>
  <p>We have expertise in Design and architectural interventions - taking a flawed product and breathing life back into it.</p>
</div>

<div class="abs sketch" style="left:0;top:3334px;width:1200px;height:399px;border-radius:0" role="img" aria-label="Pencil sketch of a suspension bridge over a river"></div>

<footer class="abs footer">
  <span class="social"></span><span class="social"></span><span class="social"></span><span class="social"></span>
</footer>

</body>
</html>
```